Atelier Vane Architecture business card

We need to update our business card. We do high end custom residential, hospitality, and wellness architecture. We focus on creating unique spaces and design around the five senses, believing that architecture's true impact is not on our surroundings, but within us. We would like to see designs are instill a sense of calm awe. They should be crisp, fresh, clean, authentic, & contemporary without being sterile, overworked, or harsh. White space is important. Alternative materials are an option if natural. We have created our own logo and would like designs to incorporate it. However, we are willing to see alternatives if the logo becomes a stumbling block and you have an alternate you suggest. Card must have the following information:
Atelier Vane Architecture, Inc.
742 Marbury Rd. NE Atlanta, GA 30319
Dominic K. Whitlow, AIA, NCARB, LEED AP BD+C
ateliervane.example

Target Market(s)

Higher net worth individuals with an appreciation for design, nature, sustainability,

Industry/Entity Type

Architect

Contact Information for Business Card

See above. The title of Owner or Architect is helpful but not necessary. Minimalism should trump additional information.

Font styles to use
Serif
Sans Serif

Requirements
Must have
• It should look professional. It must use logo
Should not have
• caligraphy, animals, anything that is cute,

```html
<!DOCTYPE html>
<html lang="en">
<head>
<meta charset="utf-8">
<title>Atelier Vane Architecture – Business Card</title>
<link rel="stylesheet" href="https://fonts.googleapis.com/css2?family=Source+Sans+3:wght@400&display=swap">
<style>
  :root {
    --backdrop: #201c1b;
    --card: #ffffff;
    --brand-green: #006c39;
    --rule-grey: #a7a9a8;
    --panel-edge: #c9cccb;
    --wordmark-grey: #5a5a5a;
    --on-green: #ffffff;
  }
  * { margin: 0; padding: 0; box-sizing: border-box; }
  html, body {
    width: 1200px;
    height: 900px;
    overflow: hidden;
    background: var(--backdrop);
    font-family: "Source Sans 3", "Myriad Pro", Arial, sans-serif;
  }
  .canvas {
    position: relative;
    width: 1200px;
    height: 900px;
    background: var(--backdrop);
  }
  .card {
    position: absolute;
    top: 55px;
    width: 460px;
    height: 789px;
    background: var(--card);
  }
  .card--front { left: 122px; }
  .card--back { left: 615px; }

  .identity-panel {
    position: absolute;
    left: 78px;
    top: 0;
    width: 308px;
    height: 384px;
    background: var(--brand-green);
    border: 1px solid var(--panel-edge);
    border-top: none;
    color: var(--on-green);
    text-align: center;
  }
  .identity-panel__name {
    position: absolute;
    top: 72px;
    width: 100%;
    font-size: 28px;
    letter-spacing: 0.3px;
  }
  .identity-panel__credentials {
    position: absolute;
    top: 114px;
    width: 100%;
    font-size: 15px;
    letter-spacing: 0.4px;
  }
  .identity-panel__company {
    position: absolute;
    top: 209px;
    width: 100%;
    font-size: 27px;
    line-height: 36px;
  }
  .identity-panel__rule {
    position: absolute;
    top: 291px;
    left: 0;
    width: 100%;
    height: 3px;
    background: var(--rule-grey);
  }
  .identity-panel__address {
    position: absolute;
    top: 305px;
    width: 100%;
    font-size: 19px;
    line-height: 27px;
  }

  .wordmark {
    position: absolute;
    left: 0;
    top: 566px;
    width: 100%;
    text-align: center;
    font-size: 28px;
    color: var(--wordmark-grey);
    letter-spacing: 1px;
  }

  .website {
    position: absolute;
    top: 374px;
    width: 100%;
    text-align: center;
    font-size: 26px;
    color: var(--brand-green);
    letter-spacing: 0.3px;
  }
</style>
</head>
<body>
  <main class="canvas">
    <section class="card card--front">
      <div class="identity-panel">
        <p class="identity-panel__name">Dominic K. Whitlow</p>
        <p class="identity-panel__credentials">AIA, NCARB, LEED AP BD+C</p>
        <p class="identity-panel__company">Atelier Vane<br>Architecture, Inc.</p>
        <div class="identity-panel__rule"></div>
        <p class="identity-panel__address">742 Marbury Rd.<br>NE Atlanta, GA 30319</p>
      </div>
      <p class="wordmark">Atelier Vane Architecture</p>
    </section>
    <section class="card card--back">
      <p class="website">ateliervane.example</p>
    </section>
  </main>
</body>
</html>
```